Personal Finance Author needs a postcard

Hi there,

I am a Canadian personal finance author and have published a new book called The Wealth Compass.

I teach Millennials how to create a 6-figure portfolio through investing (https://www.dariafelt.com/)

I'm speaking at some conferences so we were going to print some postcards to hand out to attendees with our info and calls-to-action on them.

I am looking for 4x6 (horizontal) postcard (no space needed for shipping label).

Logos, Headshots and Book Cover:
https://files.cloudvaultex.com/folders/8kQpZrT2mWvN4xLbJ7sHdYc3FgA9eUoRi?usp=sharing

Both sides will be full colour. I would like a clean and simple look. Our main sites are www.DariaFelt.com and www.TheWealthCompassBook.com if you want to get a sense of style and design.
I also uploaded a few marketing materials so you can see the existing designs.

Side 1:
Get Instant Access to your Free Resources - main headline

(small bullets underneath)
- The Wealth Compass Checklist
- Financial Worksheets
- Database of Investment Tools

DariaFelt.com/Resources

At the bottom, include "Don't forget to follow Daria Felt on social media:
Linkedin: @dariafelt7
Facebook: @thewealthcompassbook Instagram: @thewealthcompassbook Twitter: @WealthCompassBk"

Side 2:
Headline - Want to work directly with Daria and The Wealth Compass team to help you make your money grow and stay safe?

Work with us to (bullet point list)...
- Hire Daria as a Keynote Speaker
- Teach Financial Literacy Workshops
- Receive Financial Coaching

Want To Learn More About How We Can Help?
DariaFelt.com/Services

Include my contact info:
Daria Felt
Author | Speaker | Investor
daria@thewealthcompassbook.com
416-555-0187

Target Market(s)

Millennials who want to learn how to save and invest their money. I focus on stock market investing, real estate investing and entrepreneurship.

Industry/Entity Type

Financial Service

Font styles to use
Sans Serif

Colors

Designer to choose colors to be used in the design.

Requirements
Must have
• Photo of Daria Felt
• The Wealth Compass logo
• Green, Gold/Yellow to match existing colours
• modern business style postcard

```html
<!DOCTYPE html>
<html lang="en">
<head>
<meta charset="utf-8">
<title>The Wealth Compass – Postcard</title>
<link href="https://fonts.googleapis.com/css2?family=League+Gothic&family=Montserrat:wght@500;600;700&display=swap" rel="stylesheet">
<style>
  :root {
    --green: #0b6633;
    --green-dark: #075a2b;
    --gold: #e9b132;
    --ink: #2e2e2e;
    --grey-panel: #ececec;
    --grey-line: #8a8a8a;
    --stamp: #dcdcdc;
    --page: #ffffff;
    --head: "League Gothic", "Arial Narrow", sans-serif;
    --body: "Montserrat", Arial, sans-serif;
  }
  * { box-sizing: border-box; margin: 0; padding: 0; }
  html, body { width: 1200px; height: 2475px; overflow: hidden; background: var(--page); }
  .sheet { position: relative; width: 1200px; height: 2475px; }
  .card {
    position: absolute; left: 107px; width: 985px; height: 656px;
    background: #fff; box-shadow: 0 4px 18px rgba(0,0,0,.18); overflow: hidden;
  }
  .card--front { top: 546px; }
  .card--back { top: 1272px; }
  .abs { position: absolute; }

  /* front */
  .front-bg {
    left: 0; top: 22px; width: 962px; height: 610px;
    background: linear-gradient(110deg, #fff 0%, #fff 45%, #e6e6e6 62%, #e4e4e4 100%);
  }
  .portrait { background: linear-gradient(180deg, #dcdcdc 0%, #b98f7c 35%, #8a6654 55%, #1e1e22 80%); }
  .front-portrait { left: 650px; top: 95px; width: 312px; height: 537px; border-radius: 150px 150px 0 0; }
  .book { background: linear-gradient(160deg, #f5f5f2 0%, #e4e2da 60%, #c9c5b8 100%); box-shadow: 4px 6px 12px rgba(0,0,0,.3); }
  .front-book { left: 540px; top: 360px; width: 150px; height: 235px; transform: rotate(-9deg); }
  .brand {
    font-family: var(--head); font-weight: 400; color: var(--green);
    text-transform: uppercase; line-height: .92; white-space: nowrap;
  }
  .front-brand { left: 55px; top: 48px; font-size: 58px; }
  .site-url { right: 55px; top: 58px; font-family: var(--body); font-weight: 600; font-size: 20px; letter-spacing: 3px; color: #111; }
  .headline { font-family: var(--head); font-weight: 400; text-transform: uppercase; line-height: 1; white-space: nowrap; }
  .headline .g { color: var(--green); display: block; }
  .headline .y { color: var(--gold); display: block; }
  .front-headline { left: 55px; top: 195px; font-size: 74px; }
  .rule { height: 3px; background: var(--grey-line); }
  .front-rule { left: 55px; top: 341px; width: 370px; }
  .ticks { list-style: none; font-family: var(--body); }
  .ticks li { display: flex; align-items: center; gap: 14px; white-space: nowrap; }
  .ticks svg { width: 20px; height: 20px; flex: none; }
  .front-ticks { left: 55px; top: 360px; font-size: 19px; font-weight: 700; color: #111; }
  .front-ticks li { height: 32px; }
  .social-title { left: 55px; top: 492px; font-family: var(--head); font-weight: 400; font-size: 36px; line-height: 1.05; text-transform: uppercase; white-space: nowrap; }
  .social-title .y { color: var(--gold); display: block; }
  .social-title .w { color: #fff; display: block; }
  .socials { left: 55px; top: 573px; display: grid; grid-template-columns: 210px 210px; row-gap: 4px; font-family: var(--body); font-weight: 500; font-size: 14px; color: #fff; }
  .socials span { display: flex; align-items: center; gap: 6px; white-space: nowrap; }
  .socials i { width: 11px; height: 11px; background: var(--gold); border-radius: 2px; display: inline-block; }

  /* back */
  .back-headline { left: 45px; top: 34px; font-size: 48px; }
  .back-rule { left: 45px; top: 133px; width: 470px; height: 2px; }
  .back-sub { left: 45px; top: 144px; font-family: var(--body); font-weight: 600; font-size: 26px; line-height: 1.25; color: var(--ink); text-transform: uppercase; letter-spacing: .5px; white-space: nowrap; }
  .back-panel { left: 22px; top: 228px; width: 528px; height: 240px; background: var(--grey-panel); }
  .back-ticks { left: 55px; top: 248px; font-size: 18px; font-weight: 500; color: #333; }
  .back-ticks li { height: 30px; gap: 10px; }
  .back-ticks svg { width: 18px; height: 18px; }
  .learn { left: 166px; top: 380px; font-family: var(--body); white-space: nowrap; }
  .learn b { display: block; font-size: 28px; font-weight: 700; color: var(--green); letter-spacing: 1px; text-transform: uppercase; line-height: 1.1; }
  .learn span { display: block; font-size: 18px; font-weight: 600; color: #111; text-transform: uppercase; }
  .contact-band { left: 18px; top: 458px; width: 506px; height: 175px; background: var(--green-dark); }
  .back-portrait { left: 28px; top: 375px; width: 128px; height: 258px; border-radius: 64px 64px 0 0; }
  .roles { left: 168px; top: 474px; font-family: var(--body); font-weight: 700; font-size: 19px; color: #fff; letter-spacing: 1px; white-space: nowrap; }
  .contacts { left: 190px; top: 518px; font-family: var(--body); font-weight: 700; color: #fff; white-space: nowrap; }
  .contacts div { display: flex; align-items: center; gap: 12px; }
  .contacts svg { width: 20px; height: 20px; flex: none; }
  .contacts .mail { font-size: 13px; height: 26px; }
  .contacts .web { font-size: 18px; letter-spacing: 1px; height: 28px; }
  .contacts .phone { font-size: 31px; letter-spacing: 2px; height: 40px; }
  .back-book { left: 470px; top: 420px; width: 118px; height: 185px; transform: rotate(-9deg); }
  .back-brand { left: 598px; top: 66px; font-size: 30px; }
  .stamp { left: 843px; top: 55px; width: 79px; height: 80px; background: var(--stamp); }
  .address-line { left: 680px; width: 242px; height: 1px; background: #777; }
</style>
</head>
<body>
<main class="sheet">

  <!-- front side -->
  <section class="card card--front">
    <div class="abs front-bg"></div>
    <div class="abs portrait front-portrait" role="img" aria-label="Headshot photo of Daria Felt, smiling, in a dark blazer"></div>

    <svg class="abs" style="left:0;top:0" width="985" height="656" viewBox="0 0 985 656">
      <polygon points="0,480 545,480 455,632 0,632" fill="var(--green-dark)"/>
      <polygon points="440,632 700,400 962,632" fill="#fff"/>
      <polygon points="458,632 700,418 948,632" fill="var(--gold)"/>
    </svg>

    <div class="abs book front-book" role="img" aria-label="Cover of the book The Wealth Compass by Daria Felt"></div>

    <div class="abs brand front-brand">The Wealth<br>Compass</div>
    <div class="abs site-url">www.dariaFelt.com</div>

    <h1 class="abs headline front-headline">
      <span class="g">Get instant access to</span>
      <span class="y">your free resources</span>
    </h1>
    <div class="abs rule front-rule"></div>

    <ul class="abs ticks front-ticks">
      <li><svg viewBox="0 0 20 20"><rect x="1" y="3" width="15" height="15" fill="none" stroke="#777" stroke-width="1.6"/><path d="M4 10l4 4 10-12" fill="none" stroke="#777" stroke-width="1.8"/></svg>The Wealth Compass Checklist</li>
      <li><svg viewBox="0 0 20 20"><rect x="1" y="3" width="15" height="15" fill="none" stroke="#777" stroke-width="1.6"/><path d="M4 10l4 4 10-12" fill="none" stroke="#777" stroke-width="1.8"/></svg>Financial Worksheets</li>
      <li><svg viewBox="0 0 20 20"><rect x="1" y="3" width="15" height="15" fill="none" stroke="#777" stroke-width="1.6"/><path d="M4 10l4 4 10-12" fill="none" stroke="#777" stroke-width="1.8"/></svg>Database of Investment Tools</li>
    </ul>

    <h2 class="abs social-title">
      <span class="y">Don't forget to follow</span>
      <span class="w">Daria Felt on social media</span>
    </h2>
    <div class="abs socials">
      <span><i></i>@dariafelt7</span>
      <span><i></i>@thewealthcompassbook</span>
      <span><i></i>@thewealthcompassbook</span>
      <span><i></i>@WealthCompassBk</span>
    </div>
  </section>

  <!-- back side -->
  <section class="card card--back">
    <h1 class="abs headline back-headline">
      <span class="g">Want to work directly with Daria</span>
      <span class="y">and the Wealth Compass team</span>
    </h1>
    <div class="abs rule back-rule"></div>
    <p class="abs back-sub">To help you make your money<br>grow and stay safe?</p>

    <div class="abs back-panel"></div>
    <ul class="abs ticks back-ticks">
      <li><svg viewBox="0 0 20 20"><rect x="1" y="3" width="15" height="15" fill="none" stroke="#777" stroke-width="1.6"/><path d="M4 10l4 4 10-12" fill="none" stroke="#777" stroke-width="1.8"/></svg>Hire Daria as a Keynote Speaker</li>
      <li><svg viewBox="0 0 20 20"><rect x="1" y="3" width="15" height="15" fill="none" stroke="#777" stroke-width="1.6"/><path d="M4 10l4 4 10-12" fill="none" stroke="#777" stroke-width="1.8"/></svg>Teach Financial Literacy Workshops</li>
      <li><svg viewBox="0 0 20 20"><rect x="1" y="3" width="15" height="15" fill="none" stroke="#777" stroke-width="1.6"/><path d="M4 10l4 4 10-12" fill="none" stroke="#777" stroke-width="1.8"/></svg>Receive Financial Coaching</li>
    </ul>

    <div class="abs contact-band"></div>
    <div class="abs portrait back-portrait" role="img" aria-label="Headshot photo of Daria Felt in a dark blazer"></div>

    <div class="abs learn"><b>Want to learn more</b><span>About how we can help?</span></div>

    <div class="abs roles">Author | Speaker | Investor</div>
    <div class="abs contacts">
      <div class="mail"><svg viewBox="0 0 20 20"><rect x="2" y="5" width="16" height="11" fill="var(--gold)"/><path d="M2 5l8 6 8-6" fill="none" stroke="var(--green-dark)" stroke-width="1.5"/></svg>daria@thewealthcompassbook.com</div>
      <div class="web"><svg viewBox="0 0 20 20" fill="none" stroke="var(--gold)" stroke-width="1.6"><circle cx="10" cy="10" r="8"/><ellipse cx="10" cy="10" rx="3.5" ry="8"/><path d="M2 10h16M3.5 6h13M3.5 14h13"/></svg>www.DariaFelt.com</div>
      <div class="phone"><svg viewBox="0 0 20 20"><path d="M5 2l3 4-2 2c1 2.5 3.5 5 6 6l2-2 4 3-2 3C9 18 2 11 2 4z" fill="var(--gold)"/></svg>416-555-0187</div>
    </div>

    <div class="abs book back-book" role="img" aria-label="Cover of the book The Wealth Compass by Daria Felt"></div>

    <div class="abs brand back-brand">The Wealth<br>Compass</div>
    <div class="abs stamp"></div>
    <div class="abs address-line" style="top:255px"></div>
    <div class="abs address-line" style="top:320px"></div>
    <div class="abs address-line" style="top:385px"></div>
  </section>

</main>
</body>
</html>
```